Heronfield Wealth Advisors, Inc. Marketing Collateral - 401k Rollover Decisions

We are looking to create a branded one-pager marketing collateral piece talking about 401k Rollovers & the important information people should know. Rough draft of concept & content included below, and we will finalize copy later. Would include a call to action to contact us. Our website and other contact information are available at https://growwithmaplecrest.com/.

Target Market(s)

Working adults ages 55-75 with access to retirement accounts or who have a 401k account. Especially interested in appealing to people who work for small businesses, local businesses, have company stock, and other unique needs in this space.

Industry/Entity Type

Financial services

Font styles to use
Other font styles liked:
• Cambria

Requirements
Must have
• Clear message & call to action
Nice to have
• Highlight how many Americans have been changing jobs since COVID and why it would be worth working with a professional to make decisions on what to do with retirement accounts and assets. (We're working on getting that stat)
Should not have
• Too much text, don't want to inundate with text blocks

```html
<!DOCTYPE html>
<html lang="en">
<head>
<meta charset="utf-8">
<title>Heronfield Wealth Advisors – Leaving an Employer</title>
<link rel="stylesheet" href="https://fonts.googleapis.com/css2?family=Montserrat:wght@300;400;500;700;800&family=Open+Sans:wght@400;500;600&display=swap">
<style>
  :root{
    --red:#c71f2d;
    --ink:#231f20;
    --text:#3a3a3a;
    --mist:#ececec;
    --row-light:#f1f1f1;
    --row-dark:#e3e3e3;
    --white:#ffffff;
    --photo-a:#d9d9d9;
    --photo-b:#b9b3b0;
  }
  *{margin:0;padding:0;box-sizing:border-box}
  html,body{width:783px;height:1200px;overflow:hidden;background:var(--white)}
  body{position:relative;font-family:"Montserrat",sans-serif;color:var(--text)}
  .flyer{position:absolute;inset:0;overflow:hidden}

  .hero{position:absolute;left:0;top:0;width:783px;height:472px}
  .hero svg{position:absolute;inset:0}

  .brand{position:absolute;left:46px;top:62px;width:250px;text-align:center}
  .brand-mark{display:block;width:40px;height:40px;background:var(--red);margin:0 auto 16px}
  .brand-name{font-family:"Montserrat",sans-serif;font-weight:500;font-size:22px;line-height:1.2;color:var(--ink);letter-spacing:.5px}

  .headline{position:absolute;left:48px;top:255px;color:var(--white);font-size:29.5px;line-height:1.2;text-transform:uppercase;letter-spacing:-.6px}
  .headline .strong{font-weight:800;display:block}
  .headline .light{font-weight:300;display:block}
  .dots{position:absolute;left:48px;top:361px;display:flex;gap:2px}
  .dots i{width:3px;height:3px;border-radius:50%;background:var(--white)}
  .dots i:nth-child(n+4){opacity:.5}
  .lede{position:absolute;left:48px;top:374px;width:340px;font-family:"Open Sans",sans-serif;font-weight:500;font-size:19.5px;line-height:25px;color:var(--white)}

  .options{position:absolute;left:0;top:472px;width:783px;height:222px;background:var(--mist)}
  .option{position:absolute;width:300px}
  .option .badge{position:absolute;left:0;top:0;width:58px;height:58px}
  .option h3{position:absolute;left:78px;top:0;font-weight:700;font-size:14px;color:var(--ink);letter-spacing:-.3px;white-space:nowrap}
  .option p{position:absolute;left:78px;top:20px;width:230px;font-size:11.5px;line-height:14px;color:var(--text)}
  .opt-1{left:46px;top:32px}
  .opt-2{left:46px;top:126px}
  .opt-3{left:385px;top:32px}
  .opt-4{left:385px;top:126px}
  .opt-3 p,.opt-4 p{width:290px}

  .advice{position:absolute;top:712px;width:314px;font-size:11.3px;line-height:15.2px;text-align:justify;color:var(--text)}
  .advice.left{left:52px}
  .advice.right{left:413px}

  .compare{position:absolute;left:52px;top:842px;width:674px;height:295px}
  .compare svg.frame{position:absolute;inset:0}
  .compare-title{position:absolute;left:156px;top:19px;width:370px;text-align:center;color:var(--white);font-weight:700;font-size:16.5px;letter-spacing:-.4px;white-space:nowrap}
  .label{position:absolute;top:46px;font-weight:700;font-size:17px;line-height:20px;letter-spacing:-.3px}
  .label.pros{left:80px;color:var(--red)}
  .label.cons{right:72px;color:var(--ink)}
  .row{position:absolute;left:0;width:674px;display:flex}
  .cell{position:relative;width:337px;height:100%;display:flex;align-items:center}
  .cell + .cell{border-left:1px solid #d3d3d3}
  .cell svg{position:absolute;left:20px;top:50%;transform:translateY(-50%);width:30px;height:30px}
  .cell p{margin-left:76px;width:240px;font-size:12.5px;line-height:15.5px;color:var(--text)}
  .cell.con svg{left:24px}
  .cell.con p{margin-left:73px}
  .r1{top:83px;height:68px;background:var(--row-light)}
  .r2{top:151px;height:79px;background:var(--row-dark)}
  .r3{top:230px;height:65px;background:var(--row-light)}

  .contact{position:absolute;left:0;top:1137px;width:783px;height:63px;background:var(--red);display:flex;align-items:center;justify-content:center;gap:14px;color:var(--white);font-weight:500;font-size:16.5px;letter-spacing:-.2px}
  .contact span{display:flex;align-items:center;gap:5px}
  .contact svg{width:15px;height:15px}
</style>
</head>
<body>
<main class="flyer">

  <header class="hero">
    <svg viewBox="0 0 783 472" width="783" height="472">
      <defs>
        <linearGradient id="photoTone" x1="0" y1="0" x2="1" y2="1">
          <stop offset="0" stop-color="var(--photo-a)"/>
          <stop offset=".6" stop-color="#cfc6c3"/>
          <stop offset="1" stop-color="var(--photo-b)"/>
        </linearGradient>
      </defs>
      <polygon points="0,215 307,215 359,43 510,472 0,472" fill="var(--red)"/>
      <polygon role="img" aria-label="Photo of a smiling retired couple sitting together on a sofa" points="364,0 783,0 783,472 520,472" fill="url(#photoTone)" stroke="#fff" stroke-width="6"/>
      <polygon points="562,427 783,427 783,472 530,472" fill="var(--ink)"/>
      <line x1="560" y1="423" x2="783" y2="423" stroke="#fff" stroke-width="4"/>
    </svg>

    <div class="brand">
      <span class="brand-mark"></span>
      <div class="brand-name">Heronfield Wealth<br>Advisors, Inc.</div>
    </div>

    <h1 class="headline">
      <span class="strong">The most important</span>
      <span class="light">thing to realize when</span>
      <span class="strong">leaving an employer</span>
    </h1>
    <div class="dots"><i></i><i></i><i></i><i></i><i></i></div>
    <p class="lede">Is that you have options for the money that you have worked hard for and saved.</p>
  </header>

  <section class="options">
    <div class="option opt-1">
      <svg class="badge" viewBox="0 0 58 58">
        <circle cx="29" cy="29" r="27" fill="none" stroke="#c71f2d" stroke-width="1.2" stroke-dasharray="2 2"/>
        <circle cx="29" cy="29" r="22" fill="#fff" stroke="#231f20" stroke-width="2.5"/>
        <rect x="19" y="21" width="20" height="15" fill="none" stroke="#231f20" stroke-width="1.2"/>
        <line x1="22" y1="26" x2="36" y2="26" stroke="#231f20" stroke-width="1"/>
        <line x1="22" y1="30" x2="32" y2="30" stroke="#231f20" stroke-width="1"/>
        <circle cx="47" cy="8" r="8" fill="#231f20"/>
        <text x="47" y="11" font-size="8" fill="#fff" text-anchor="middle" font-family="Montserrat,sans-serif">01</text>
      </svg>
      <h3>LEAVE IT</h3>
      <p>Most employer plans allow you to leave the funds within the qualified plan</p>
    </div>
    <div class="option opt-2">
      <svg class="badge" viewBox="0 0 58 58">
        <circle cx="29" cy="29" r="27" fill="none" stroke="#c71f2d" stroke-width="1.2" stroke-dasharray="2 2"/>
        <circle cx="29" cy="29" r="22" fill="#fff" stroke="#231f20" stroke-width="2.5"/>
        <rect x="21" y="19" width="14" height="20" rx="2" fill="none" stroke="#231f20" stroke-width="1.2"/>
        <path d="M35 23 q4 0 4 4 v8" fill="none" stroke="#231f20" stroke-width="1.2"/>
        <circle cx="47" cy="8" r="8" fill="#231f20"/>
        <text x="47" y="11" font-size="8" fill="#fff" text-anchor="middle" font-family="Montserrat,sans-serif">02</text>
      </svg>
      <h3>ROLL IT</h3>
      <p>Depending on the type of qualified plan, you can roll the funds over from the employer plan to an IRA.</p>
    </div>
    <div class="option opt-3">
      <svg class="badge" viewBox="0 0 58 58">
        <circle cx="29" cy="29" r="27" fill="none" stroke="#c71f2d" stroke-width="1.2" stroke-dasharray="2 2"/>
        <circle cx="29" cy="29" r="22" fill="#fff" stroke="#231f20" stroke-width="2.5"/>
        <rect x="18" y="23" width="16" height="11" fill="none" stroke="#231f20" stroke-width="1.2"/>
        <path d="M34 26 h5 l3 4 v4 h-8z" fill="none" stroke="#231f20" stroke-width="1.2"/>
        <circle cx="23" cy="36" r="2" fill="#231f20"/><circle cx="37" cy="36" r="2" fill="#231f20"/>
        <circle cx="47" cy="8" r="8" fill="#231f20"/>
        <text x="47" y="11" font-size="8" fill="#fff" text-anchor="middle" font-family="Montserrat,sans-serif">03</text>
      </svg>
      <h3>MOVE IT</h3>
      <p>If you've started working at a new company, they will often have their own qualified plan available that you can move your old company's funds to.</p>
    </div>
    <div class="option opt-4">
      <svg class="badge" viewBox="0 0 58 58">
        <circle cx="29" cy="29" r="27" fill="none" stroke="#c71f2d" stroke-width="1.2" stroke-dasharray="2 2"/>
        <circle cx="29" cy="29" r="22" fill="#fff" stroke="#231f20" stroke-width="2.5"/>
        <rect x="20" y="28" width="18" height="10" fill="none" stroke="#231f20" stroke-width="1.2"/>
        <circle cx="29" cy="23" r="4" fill="none" stroke="#231f20" stroke-width="1.2"/>
        <circle cx="29" cy="33" r="2" fill="#231f20"/>
        <circle cx="47" cy="8" r="8" fill="#231f20"/>
        <text x="47" y="11" font-size="8" fill="#fff" text-anchor="middle" font-family="Montserrat,sans-serif">04</text>
      </svg>
      <h3>TAKE IT</h3>
      <p>There is the option to take the account in cash, but it is not typically advisable due to the tax and potential penalty implications.</p>
    </div>
  </section>

  <p class="advice left">It is important to work with a fiduciary to help you evaluate your options and the pros and cons of them. A fiduciary is someone who is obligated to provide you unbiased advice and disclose any conflicts of interest in their recommendations. It can be particularly important to work with a fiduciary if you are retiring early or are generally confused about all of the information and misinformation out there.</p>
  <p class="advice right">We recommend working with an expert who has experience with a multitude of different types of qualified plans such as 401(k), 403(b), Employee Stock Ownership Plans, SEP IRAs, etc. Not all plan types are eligible for rollovers, and even if they are, they may vary in the types of plans that they can be rolled in to.</p>

  <section class="compare">
    <svg class="frame" viewBox="0 0 674 295" width="674" height="295">
      <rect x="0" y="32" width="674" height="51" fill="#e2e2e2"/>
      <rect x="0" y="32" width="67" height="51" rx="5" fill="var(--red)"/>
      <rect x="5" y="32" width="62" height="51" fill="var(--red)"/>
      <rect x="609" y="32" width="65" height="51" rx="5" fill="var(--ink)"/>
      <rect x="609" y="32" width="60" height="51" fill="var(--ink)"/>
      <path d="M156 0 H526 V44 Q526 58 512 58 H170 Q156 58 156 44 Z" fill="var(--ink)"/>
      <path d="M125 0 Q152 2 156 30 V0 Z" fill="var(--ink)"/>
      <path d="M557 0 Q530 2 526 30 V0 Z" fill="var(--ink)"/>
      <g fill="#fff">
        <path d="M27 74 v-10 h4 l4 -7 q3 0 2 4 l-1 3 h6 q2 0 2 2 l-2 8 q-1 2 -3 2 h-8z"/>
        <rect x="29" y="44" width="10" height="7" rx="1.5"/>
      </g>
      <g fill="#fff">
        <path d="M635 52 v10 h4 l4 7 q3 0 2 -4 l-1 -3 h6 q2 0 2 -2 l-2 -8 q-1 -2 -3 -2 h-8z"/>
        <rect x="636" y="41" width="10" height="7" rx="1.5"/>
      </g>
    </svg>
    <div class="compare-title">ROLLING OVER 401(K) ASSETS TO IRA</div>
    <div class="label pros">PROS</div>
    <div class="label cons">CONS</div>

    <div class="row r1">
      <div class="cell pro">
        <svg viewBox="0 0 30 30"><circle cx="9" cy="21" r="7" fill="none" stroke="#231f20" stroke-width="1.3"/><text x="9" y="25" font-size="10" text-anchor="middle" fill="#231f20">$</text><path d="M14 14 L26 4 M20 4 h6 v6" fill="none" stroke="#231f20" stroke-width="1.3"/></svg>
        <p>Typically more investment choices in an IRA</p>
      </div>
      <div class="cell con">
        <svg viewBox="0 0 30 30"><path d="M15 3 l9 3 v8 q0 7 -9 11 q-9 -4 -9 -11 v-8z" fill="none" stroke="#231f20" stroke-width="1.3"/><path d="M11 14 l3 3 l5 -6" fill="none" stroke="#231f20" stroke-width="1.3"/></svg>
        <p>Less protection from creditors</p>
      </div>
    </div>
    <div class="row r2">
      <div class="cell pro">
        <svg viewBox="0 0 30 30"><circle cx="8" cy="10" r="3" fill="none" stroke="#231f20" stroke-width="1.3"/><circle cx="15" cy="8" r="3" fill="none" stroke="#231f20" stroke-width="1.3"/><circle cx="22" cy="10" r="3" fill="none" stroke="#231f20" stroke-width="1.3"/><path d="M3 27 v-8 q5 -5 10 0 M10 27 v-9 q5 -5 10 0 v9 M17 19 q5 -5 10 0 v8" fill="none" stroke="#231f20" stroke-width="1.3"/></svg>
        <p>Ability to make contributions to the account even after leaving your former employer</p>
      </div>
      <div class="cell con">
        <svg viewBox="0 0 30 30"><path d="M13 28 v-14 q0 -2 2 -2 q2 0 2 2 v6 l5 1 q2 1 1 4 l-1 3" fill="none" stroke="#231f20" stroke-width="1.3"/><circle cx="15" cy="5" r="2" fill="none" stroke="#231f20" stroke-width="1.3"/><circle cx="6" cy="8" r="2" fill="none" stroke="#231f20" stroke-width="1.3"/><circle cx="24" cy="8" r="2" fill="none" stroke="#231f20" stroke-width="1.3"/></svg>
        <p>Less access to funds prior to age 59½</p>
      </div>
    </div>
    <div class="row r3">
      <div class="cell pro">
        <svg viewBox="0 0 30 30"><circle cx="10" cy="9" r="4" fill="none" stroke="#231f20" stroke-width="1.3"/><circle cx="22" cy="7" r="4" fill="none" stroke="#231f20" stroke-width="1.3"/><path d="M3 27 v-6 q7 -7 14 0 v6 M17 21 q5 -7 11 -1 v7" fill="none" stroke="#231f20" stroke-width="1.3"/></svg>
        <p>Choice of investment custodian and investment advisor you work with</p>
      </div>
      <div class="cell con">
        <svg viewBox="0 0 30 30"><circle cx="11" cy="8" r="4" fill="none" stroke="#231f20" stroke-width="1.3"/><path d="M3 22 q1 -8 8 -8 q7 0 8 8" fill="none" stroke="#231f20" stroke-width="1.3"/><rect x="3" y="22" width="24" height="5" fill="none" stroke="#231f20" stroke-width="1.3"/><rect x="18" y="14" width="9" height="8" fill="none" stroke="#231f20" stroke-width="1.3"/></svg>
        <p>RMDs on funds at age 72 regardless if you are still working</p>
      </div>
    </div>
  </section>

  <footer class="contact">
    <span><svg viewBox="0 0 16 16"><path d="M3 1 l3 0 l1 4 l-2 1 q1 3 4 5 l1 -2 l4 1 v3 q-1 2 -3 2 q-10 -2 -12 -12 q0 -2 2 -2z" fill="#fff"/></svg>555-210-4378</span>
    <span><svg viewBox="0 0 16 16"><rect x="1" y="3" width="14" height="10" fill="#fff"/><path d="M1 3 l7 6 l7 -6" fill="none" stroke="#c71f2d" stroke-width="1.3"/></svg>info@growwithmaplecrest.com</span>
    <span><svg viewBox="0 0 16 16"><circle cx="8" cy="8" r="6.5" fill="none" stroke="#fff" stroke-width="1.3"/><ellipse cx="8" cy="8" rx="3" ry="6.5" fill="none" stroke="#fff" stroke-width="1.1"/><line x1="1.5" y1="8" x2="14.5" y2="8" stroke="#fff" stroke-width="1.1"/></svg>www.growwithmaplecrest.com</span>
  </footer>

</main>
</body>
</html>
```